Lorn Systems

Looking for a web site design to market our services/applications
We write and supply bespoke web applications for the offshore and construction industries
Our initial product is Velk - rope access equipment management
Our buyers will be Rope Access companies via trade associations such as OBWEN and KLUDE
we have a logo designed see it attached we would like to see crisp professional designs based around these colours and design
we will supply web copy later
looking for home, services, blog, contact us, order and a general template (privacy, site map, T&C) pages
Updates
This payment will be for the homepage only
We can discuss other options (pages) with the successful designer
Regards
Brian
Industry/Entity Type
Construction
Look and feel
Each slider illustrates characteristics of the customer's brand and the style your logo design should communicate.

```html
<!DOCTYPE html>
<html lang="en">
<head>
<meta charset="utf-8">
<title>Lorn Systems — Home</title>
<link href="https://fonts.googleapis.com/css2?family=Arimo:wght@400;700&family=Open+Sans:wght@400;600;700&display=swap" rel="stylesheet">
<style>
:root{
  --navy:#2e3192;
  --nav:#4a4fa8;
  --nav-active:#6a70c0;
  --band:#3f43a3;
  --footer:#3f449f;
  --footer-bar:#4b51ad;
  --sky:#8fa4d8;
  --text:#222;
  --muted:#555;
  --light-bg:#f3f3f5;
  --white:#fff;
  --frame:#d9daeb;
}
*{box-sizing:border-box;margin:0;padding:0}
html,body{width:1200px;height:2494px;overflow:hidden}
body{position:relative;background:var(--white);font-family:"Arimo",Arial,sans-serif;color:var(--text)}
.abs{position:absolute}

/* header */
.phone{left:128px;top:18px;display:flex;align-items:center;gap:10px;font-size:17px;color:var(--navy)}
.search{left:783px;top:15px;width:194px;height:30px;background:var(--navy);color:#fff;font-size:12px;display:flex;align-items:center;justify-content:space-between;padding:0 10px}
.lang{left:1030px;top:15px;width:45px;height:30px;background:#dfe0ee;font-size:12px;display:flex;align-items:center;justify-content:center;gap:5px;color:#222}
.brand{left:125px;top:60px;display:flex;align-items:center;gap:14px}
.brand-mark{width:84px;height:84px;border-radius:10px;background:linear-gradient(#f2f3f7,#c9cbd6)}
.brand-name{font-size:32px;line-height:34px;color:var(--navy);font-weight:400;width:200px}
.nav{left:471px;top:98px;width:604px;height:48px;background:var(--nav);display:flex;box-shadow:0 6px 10px rgba(0,0,0,.25)}
.nav a{color:#fff;text-decoration:none;font-size:21px;display:flex;align-items:center;justify-content:center;height:100%}
.nav a.active{background:var(--nav-active)}

/* hero */
.hero{left:0;top:146px;width:1200px;height:480px;background:linear-gradient(90deg,#2b3245 0%,#5d6c8c 28%,#c7cde0 45%,#a3b4e0 60%,var(--sky) 100%)}
.hero-copy{left:600px;top:222px;width:490px;text-align:center;font-size:31px;line-height:42px;color:#111}
.btn-order{left:725px;top:322px;width:237px;height:64px;background:var(--navy);color:#fff;font-size:31px;display:flex;align-items:center;justify-content:center;border-radius:3px}
.dots{left:938px;top:574px;display:flex;gap:13px}
.dots span{width:17px;height:17px;border-radius:50%;background:#fff;box-shadow:0 1px 2px rgba(0,0,0,.4)}
.dots span.on{background:var(--navy)}
.hero-shadow{left:0;top:626px;width:1200px;height:20px;background:linear-gradient(rgba(0,0,0,.18),rgba(0,0,0,0))}

/* welcome */
.welcome-bg{left:0;top:646px;width:1200px;height:436px;background:linear-gradient(#fff 40%,var(--light-bg))}
.welcome-title{left:0;top:682px;width:1200px;display:flex;justify-content:center;align-items:center;gap:14px;font-size:34px;color:var(--navy)}
.deco{display:flex;gap:8px;align-items:center}
.deco i{display:block;width:9px;height:9px;border-radius:50%;background:var(--navy)}
.deco i:nth-child(1){opacity:.3}.deco i:nth-child(2){opacity:.5}.deco i:nth-child(3){opacity:.7}
.deco.right i:nth-child(3){opacity:.3}.deco.right i:nth-child(1){opacity:.9}
.about-photo{left:127px;top:790px;width:293px;height:225px;border:3px solid #8c90c9;background:linear-gradient(135deg,#7a6a5c,#2a2a30 55%,#54595f)}
.about-text{left:444px;top:786px;width:631px;font-size:16px;line-height:25px;color:#222}
.btn-read{left:931px;top:975px;width:144px;height:40px;background:var(--navy);color:#fff;font-size:20px;display:flex;align-items:center;justify-content:center}

/* services */
.band{left:0;top:1082px;width:1200px;height:51px;background:var(--band)}
.band-title{left:127px;top:1087px;font-size:33px;color:#fff}
.band-arrows{left:1015px;top:1094px}
.card-photo{top:1188px;width:296px;height:243px;border:6px solid var(--frame);border-radius:4px}
.card-title{top:1448px;width:330px;text-align:center;font-size:21px;color:var(--navy)}
.card-text{top:1488px;width:240px;text-align:center;font-size:16px;line-height:25px;color:var(--muted)}
.btn-learn{top:1604px;width:128px;height:35px;background:linear-gradient(#4c51b0,var(--navy));color:#fff;font-size:16px;display:flex;align-items:center;justify-content:center}

/* blog */
.blog-bg{left:0;top:1723px;width:1200px;height:471px;background:linear-gradient(var(--light-bg),#fff 45%,#f7f7f9)}
.blog-title{left:127px;top:1748px;font-size:35px;color:var(--navy)}
.blog-rule{left:127px;top:1796px;width:948px;border-top:3px dotted #c9cad3}
.avatar{left:127px;width:131px;height:131px;border-radius:50%;border:4px solid var(--frame);background:linear-gradient(#eceef4,#bcc0cf)}
.post-title{left:302px;font-size:17px;color:var(--navy)}
.post-date{left:302px;font-size:13px;color:var(--navy)}
.post-text{left:302px;width:680px;font-size:12.5px;line-height:25px;color:#222}

/* footer */
.footer{left:0;top:2194px;width:1200px;height:257px;background:var(--footer);box-shadow:0 -8px 14px rgba(0,0,0,.18);font-family:"Open Sans",Arial,sans-serif;color:#fff}
.map{left:125px;top:41px;width:247px;height:177px;background:linear-gradient(135deg,#e8e5dc,#d4d8cf 55%,#c9d3e2);border:3px solid #fff;box-shadow:0 3px 6px rgba(0,0,0,.35)}
.f-head{font-size:17px;font-weight:600;letter-spacing:.3px}
.f-address{left:408px;top:40px;width:210px}
.f-address p{font-size:12.5px;font-weight:700;line-height:22.5px;margin-top:8px}
.divider{top:68px;height:140px;border-left:1px solid rgba(255,255,255,.3)}
.f-links{left:687px;top:40px}
.f-links ul{list-style:none;margin-top:8px}
.f-links li{font-size:16px;line-height:25px}
.f-follow{left:914px;top:40px}
.social{display:grid;grid-template-columns:repeat(4,30px);gap:32px 11px;margin-top:16px}
.social span{width:30px;height:30px;border-radius:4px;background:rgba(255,255,255,.85)}
.footer-bar{left:0;top:2451px;width:1200px;height:43px;background:var(--footer-bar);font-family:"Open Sans",Arial,sans-serif;color:#fff;font-size:10px;font-weight:700}
.copyright{left:550px;top:15px}
.legal{left:943px;top:15px;display:flex;gap:7px}
</style>
</head>
<body>

<header>
  <div class="abs phone">
    <svg width="18" height="18" viewBox="0 0 24 24"><path fill="#2e3192" d="M6.6 10.8a15.1 15.1 0 0 0 6.6 6.6l2.2-2.2c.3-.3.7-.4 1-.2 1.1.4 2.3.6 3.6.6.6 0 1 .4 1 1V20c0 .6-.4 1-1 1A17 17 0 0 1 3 4c0-.6.4-1 1-1h3.5c.6 0 1 .4 1 1 0 1.3.2 2.5.6 3.6.1.3 0 .7-.2 1z"/></svg>
    <span>+00-55501234</span>
  </div>
  <div class="abs search"><span>Search..</span>
    <svg width="16" height="16" viewBox="0 0 24 24"><circle cx="10" cy="10" r="6.5" fill="none" stroke="#fff" stroke-width="3"/><path d="M15 15l6 6" stroke="#fff" stroke-width="3"/></svg>
  </div>
  <div class="abs lang">EN <svg width="8" height="6"><path d="M0 0h8L4 6z" fill="#222"/></svg></div>
  <div class="abs brand">
    <div class="brand-mark"></div>
    <div class="brand-name">Lorn Systems</div>
  </div>
  <nav class="abs nav">
    <a class="active" style="width:97px">Home</a>
    <a style="width:121px">Services</a>
    <a style="width:92px">Blog</a>
    <a style="width:158px">Contact Us</a>
    <a style="width:136px">Order</a>
  </nav>
</header>

<section>
  <div class="abs hero" role="img" aria-label="Rope access technicians abseiling down a glass building facade at dusk"></div>
  <p class="abs hero-copy">Want to purchase &nbsp;Velk - rope access equipment then order now</p>
  <div class="abs btn-order">ORDER NOW</div>
  <div class="abs dots"><span class="on"></span><span></span><span></span><span></span><span></span></div>
  <div class="abs hero-shadow"></div>
</section>

<section>
  <div class="abs welcome-bg"></div>
  <h1 class="abs welcome-title" style="font-weight:400">
    <span class="deco"><i></i><i></i><i></i><i></i></span>
    Welcome to Lorn Systems
    <span class="deco right"><i></i><i></i><i></i><i></i></span>
  </h1>
  <div class="abs about-photo" role="img" aria-label="Close-up of a figure-eight descender with red climbing rope"></div>
  <p class="abs about-text">Lorem Ipsum is simply dummy text of the printing and typesetting industry. Lorem Ipsum has been the industry's standard dummy text ever since the 1500s, when an unknown printer took a galley of type and scrambled it to make a type specimen book. It has survived not only five centuries, but also the leap into electronic typesetting, remaining essentially unchanged. It was popularised in the 1960s with the release of Letraset sheets containing Lorem Ipsum passages.</p>
  <div class="abs btn-read">Read More</div>
</section>

<section>
  <div class="abs band"></div>
  <h2 class="abs band-title" style="font-weight:400">Our Services</h2>
  <svg class="abs band-arrows" width="60" height="24" viewBox="0 0 60 24"><path d="M14 3L5 12l9 9M42 3l9 9-9 9" fill="none" stroke="#fff" stroke-width="2"/><path d="M30 2v20" stroke="rgba(255,255,255,.35)"/></svg>

  <div class="abs card-photo" style="left:127px;background:linear-gradient(135deg,#5b6296,#3a3f74 60%,#6d73a8)" role="img" aria-label="Hand touching a digital interface with application icons"></div>
  <div class="abs card-photo" style="left:453px;background:linear-gradient(135deg,#c79a2a,#3b3b3f 55%,#5e5b55)" role="img" aria-label="Yellow rope access descender device"></div>
  <div class="abs card-photo" style="left:787px;background:linear-gradient(135deg,#8a7866,#2c2d3a 55%,#4c4e60)" role="img" aria-label="Figure-eight descender with red rope"></div>

  <h3 class="abs card-title" style="left:110px;font-weight:400">Lorem Ipsum is simply text</h3>
  <h3 class="abs card-title" style="left:439px;font-weight:400">Lorem Ipsum is simply text</h3>
  <h3 class="abs card-title" style="left:770px;font-weight:400">Lorem Ipsum is simply text</h3>
  <p class="abs card-text" style="left:155px">dummy text of the printing and typesetting industry. Lorem Ipsum has been the industry's standard dummy text ever</p>
  <p class="abs card-text" style="left:484px">dummy text of the printing and typesetting industry. Lorem Ipsum has been the industry's standard dummy text ever</p>
  <p class="abs card-text" style="left:815px">dummy text of the printing and typesetting industry. Lorem Ipsum has been the industry's standard dummy text ever</p>
  <div class="abs btn-learn" style="left:217px">Learn More</div>
  <div class="abs btn-learn" style="left:541px">Learn More</div>
  <div class="abs btn-learn" style="left:871px">Learn More</div>
</section>

<section>
  <div class="abs blog-bg"></div>
  <h2 class="abs blog-title" style="font-weight:400">Recent Blog</h2>
  <div class="abs blog-rule"></div>

  <div class="abs avatar" style="top:1834px" role="img" aria-label="Portrait of a blog author"></div>
  <h3 class="abs post-title" style="top:1836px;font-weight:400">Lorem Ipsum is simply text</h3>
  <p class="abs post-date" style="top:1858px">October 6th,2014</p>
  <p class="abs post-text" style="top:1883px">Lorem Ipsum is simply dummy text of the printing and typesetting industry. Lorem Ipsum has been the industry's standard dummy text ever since the 1500s, when an unknown printer took a galley of type and scrambled it to make a type specimen book. dummy text of the printingcontaining Lorem Ipsum passages.</p>

  <div class="abs avatar" style="top:2006px" role="img" aria-label="Portrait of a blog author"></div>
  <h3 class="abs post-title" style="top:2016px;font-weight:400">Lorem Ipsum is simply text</h3>
  <p class="abs post-date" style="top:2038px">October 7th,2014</p>
  <p class="abs post-text" style="top:2063px">Lorem Ipsum is simply dummy text of the printing and typesetting industry. Lorem Ipsum has been the industry's standard dummy text ever since the 1500s, when an unknown printer took a galley of type and scrambled it to make a type specimen book. dummy text of the printingcontaining Lorem Ipsum passages.</p>
</section>

<footer>
  <div class="abs footer">
    <div class="abs map" role="img" aria-label="Street map showing the office location"></div>
    <div class="abs f-address">
      <h4 class="f-head">Address</h4>
      <p>Lorem Ipsum is simply dummy text of the printing and types setting industry<br>Phone: +0055501234<br>Email: Lorem Ipsum is simply</p>
    </div>
    <div class="abs divider" style="left:634px"></div>
    <div class="abs f-links">
      <h4 class="f-head">Important Links</h4>
      <ul><li>Home</li><li>Services</li><li>Blog</li><li>Contact Us</li><li>Order</li></ul>
    </div>
    <div class="abs divider" style="left:872px"></div>
    <div class="abs f-follow">
      <h4 class="f-head">Fallow Us</h4>
      <div class="social"><span></span><span></span><span></span><span></span><span></span><span></span><span></span><span></span></div>
    </div>
  </div>
  <div class="abs footer-bar">
    <span class="abs copyright">All Rights Reserved</span>
    <span class="abs legal"><span>Site Map</span>|<span>Privacy</span>|<span>Site Credits</span></span>
  </div>
</footer>

</body>
</html>
```